Billboard design - consider what a billboard is

Design a billboard using my logo - Billboard is 6m x 3m
A Billboard is advertising for my company that is on a big sign.

Has to be clean and easy to read, and ideally highlights that we are Residential and Commercial builders.

Keep it clean and easy to read

The contact number for the board is

027 584 9071
www.fernridgebuildworks.co.nz
info@fernridgebuildworks.co.nz

Doesnt have to have all contact details if it doesnt fit

Has to catch peoples attention to contact us if they need a builder

Can you please change the sign to be all white writing, with black background ?
Updates

Please consider what a billboard is...

The design needs to be suitable for a billboard..

Target Market(s)

people driving past

Industry/Entity Type

Construction

Logo Text

Wellington Builder, website email address, contact number

Colors
0054AA
0677BA
7BADD7
CADEEF
E8F1F8

Requirements
Must have
• Easy to read
Nice to have
• easy to read, can clearly see contact details

```html
<!DOCTYPE html>
<html lang="en">
<head>
<meta charset="utf-8">
<title>Fernridge Buildworks Billboard</title>
<link rel="stylesheet" href="https://fonts.googleapis.com/css2?family=Oswald:wght@500;600&family=Roboto+Condensed:wght@500;700&display=swap">
<style>
  :root {
    --brand-deep: #0557A6;
    --brand-mid: #0677BA;
    --brand-soft: #7BADD7;
    --brand-pale: #CADEEF;
    --brand-mist: #E8F1F8;
    --logo-blue: #5A8BCB;
    --paper: #FFFFFF;
    --ink-light: #FFFFFF;
  }
  html, body {
    margin: 0;
    padding: 0;
    width: 1200px;
    height: 601px;
    overflow: hidden;
    background: var(--paper);
  }
  .billboard {
    position: relative;
    width: 1200px;
    height: 601px;
    background: var(--paper);
  }
  .billboard-art {
    position: absolute;
    inset: 0;
    width: 1200px;
    height: 601px;
    display: block;
  }
  .accent-stripe { fill: var(--brand-mid); }
  .contact-band { fill: var(--brand-deep); }
  .brand-mark { fill: var(--logo-blue); }
  .brand-name {
    fill: var(--logo-blue);
    font-family: "Roboto Condensed", "Arial Narrow", sans-serif;
    font-weight: 700;
  }
  .phone-number {
    fill: var(--brand-deep);
    font-family: "Oswald", "Roboto Condensed", sans-serif;
    font-weight: 600;
  }
  .contact-line {
    fill: var(--ink-light);
    font-family: "Roboto Condensed", "Arial Narrow", sans-serif;
    font-weight: 500;
  }
</style>
</head>
<body>
<main class="billboard">
  <svg class="billboard-art" viewBox="0 0 2275 1139" preserveAspectRatio="none" xmlns="http://www.w3.org/2000/svg">
    <defs>
      <linearGradient id="glassBand" x1="0" y1="0" x2="1" y2="1">
        <stop offset="0" stop-color="var(--brand-mist)"/>
        <stop offset="0.5" stop-color="var(--brand-pale)"/>
        <stop offset="1" stop-color="var(--brand-soft)"/>
      </linearGradient>
      <linearGradient id="towerTones" x1="0" y1="0" x2="0.6" y2="1">
        <stop offset="0" stop-color="#DCE3EA"/>
        <stop offset="0.3" stop-color="#8FA7BF"/>
        <stop offset="0.55" stop-color="#6E5E52"/>
        <stop offset="1" stop-color="#3A3A3D"/>
      </linearGradient>
    </defs>

    <polygon class="accent-stripe" points="0,0 430,0 1028,688 700,1139 0,1139"/>
    <polygon fill="url(#glassBand)" points="0,0 375,0 972,688 640,1139 0,1139"/>
    <polygon fill="url(#towerTones)" points="0,0 330,0 915,688 610,1139 0,1139"
             role="img" aria-label="Photo of a tall dark glass skyscraper seen from below against a cloudy blue sky"/>

    <polygon class="contact-band" points="680,863 2275,863 2275,1088 485,1088"/>

    <g class="brand-lockup" aria-label="Fernridge Buildworks">
      <rect class="brand-mark" x="1672" y="214" width="74" height="74"/>
      <text class="brand-name" x="1770" y="292" font-size="160" textLength="390" lengthAdjust="spacingAndGlyphs">Fernridge</text>
      <text class="brand-name" x="1770" y="342" font-size="50" textLength="390" lengthAdjust="spacingAndGlyphs">BUILDWORKS</text>
    </g>

    <text class="phone-number" x="1105" y="785" font-size="250" textLength="1085" lengthAdjust="spacingAndGlyphs">027 584 9071</text>

    <text class="contact-line" x="1130" y="954" font-size="84" textLength="1060" lengthAdjust="spacingAndGlyphs">www.fernridgebuildworks.co.nz</text>
    <text class="contact-line" x="1115" y="1040" font-size="84" textLength="1075" lengthAdjust="spacingAndGlyphs">info@fernridgebuildworks.co.nz</text>
  </svg>
</main>
</body>
</html>
```